Australian Craft Distillery needs poster layout for its awesome Manifesto

Brass Fern's a small craft distillery based in the Kelp Hollow of Western Australia producing award-winning vodkas and gin. Check out our website www.brassferns.com.au to get a feel for our design aesthetic, especially from our bottle design. We are "Hand Crafted Spirits - From the Kelp Hollow". Everything we do reflects that.
We have a manifesto - The Brass Fern's Manifesto -that we proudly display in our tasting room, and was used as a basis for an artwork in our entry.
We've had a number of customers ask to buy a poster of the manifesto (attached) so I want to commission a more professional design than the current layout which was put together in Word! (yes I know, I'm sorry, I did move it into Illustrator later).
I think the text flows in a sequential order so I'm looking for a design that you read from start to finish rather than a random collection of statements. I'd like to include our logo in the design somewhere but it doesn't have to be front and centre. There is a secondary logo device as well - the interlocked B and F on the label which could be used. I'm assuming the print will be simple black on either a plain background or a "craft background" similar to the labels. Our current fonts are SchmutzICG for text and VeneerTwo for headings. The label uses Haymaker and Gin-Rough.
Print size will be A3 (prefer the design to be to this proportion and portrait orientation) and bigger up to A1. We'll print the final design on the back of t-shirts for staff as well. If I was going to sum up our style in a couple of words it would be "intelligently irreverent" Have fun with this, I certainly did writing it!

```html
<!DOCTYPE html>
<html lang="en">
<head>
<meta charset="utf-8">
<title>The Brass Fern's Manifesto</title>
<link rel="stylesheet" href="https://fonts.googleapis.com/css2?family=Allerta+Stencil&family=Oswald:wght@500&family=Special+Elite&display=swap">
<style>
  :root {
    --frame-outer: #6a5d59;
    --frame-cream: #e5c795;
    --frame-tan: #c9a574;
    --board: #2f312c;
    --ink: #f4efe4;
    --mark: #3d4039;
  }
  * { margin: 0; padding: 0; box-sizing: border-box; }
  html, body {
    width: 851px; height: 1200px; overflow: hidden;
    background: var(--frame-outer);
  }
  .poster {
    position: relative; width: 851px; height: 1200px;
    background: var(--frame-outer);
  }
  .poster__edge {
    position: absolute; left: 14px; top: 16px; right: 14px; bottom: 16px;
    background: var(--frame-cream);
    border-radius: 10px;
    box-shadow: inset 0 0 18px var(--frame-tan);
  }
  .poster__board {
    position: absolute; left: 44px; top: 52px; width: 762px; height: 1103px;
    background: var(--board);
    border-radius: 26px;
    color: var(--ink);
    text-align: center;
    overflow: hidden;
  }
  .brand-mark {
    position: absolute;
    font-family: "Special Elite", "Georgia", serif;
    font-size: 26px;
    color: var(--mark);
    white-space: nowrap;
  }
  .brand-mark--right { left: 572px; top: 350px; }
  .brand-mark--left { left: 18px; top: 650px; }
  .title {
    position: absolute; left: 0; right: 0; top: 72px;
    font-family: "Allerta Stencil", "Arial Narrow", sans-serif;
    font-size: 39px; letter-spacing: 2px;
    text-transform: uppercase; font-weight: 400;
    white-space: nowrap;
  }
  .subtitle {
    position: absolute; left: 0; right: 0; top: 144px;
    font-family: "Oswald", "Arial Narrow", sans-serif;
    font-weight: 500; font-size: 24px;
    text-transform: uppercase; letter-spacing: 0.5px;
  }
  .section {
    position: absolute; left: 0; right: 0;
    font-family: "Special Elite", "Georgia", serif;
    font-size: 17.5px; line-height: 29px;
    list-style: none; white-space: nowrap;
  }
  .section--first { top: 204px; }
  .section--then { top: 378px; }
  .section--finally { top: 694px; }
</style>
</head>
<body>
<main class="poster">
  <div class="poster__edge"></div>
  <section class="poster__board">
    <span class="brand-mark brand-mark--right">Brass Fern's</span>
    <span class="brand-mark brand-mark--left">Brass Fern's</span>

    <h1 class="title">The Brass Fern's Manifesto</h1>
    <p class="subtitle">(Our thoughts on life, a.k.a. how to be better)</p>

    <ul class="section section--first">
      <li>first...</li>
      <li>• Work Smart • Love Hard • Play Often • Sleep More •</li>
      <li>• Stay Present • Be Local • Embrace Silly • Get Dirty (but) Stay Clean •</li>
      <li>• Laugh • Cry • Run • Dance • Sing •</li>
      <li>• Stop That (and) Slow down •</li>
    </ul>

    <ul class="section section--then">
      <li>then ...</li>
      <li>• Celebrate others success • Don’t be shit •</li>
      <li>• Have one thing you are awesome at •</li>
      <li>• Get off your phone • Show some fucking passion •</li>
      <li>• Make something • Making money doesn’t count • Making babies does •</li>
      <li>• Never stop exploring, never stop learning, share that with others •</li>
      <li>• We all fuck up. Make good, learn, be better and move on •</li>
      <li>• Life is far too short, squeeze every drop out of it •</li>
      <li>and, of course ...</li>
      <li>• Drink better •</li>
    </ul>

    <ul class="section section--finally">
      <li>and finally ...</li>
      <li>• Sometimes you just won’t understand •</li>
      <li>• An argument is not a fight •</li>
      <li>• You are not as important as you think •</li>
      <li>• You are more loved than you think •</li>
      <li>• Its ok to do things alone •</li>
      <li>• Its ok not to be busy •</li>
      <li>• There is no good reason to do a half arsed job •</li>
      <li>• Teaching is the best way of learning •</li>
      <li>• The past is important, what you do next is much more so •</li>
      <li>• Change is inevitable, roll with it •</li>
      <li>• Success is whatever you decide it to be •</li>
    </ul>
  </section>
</main>
</body>
</html>
```